Velmont Systems Business Card

Utilize the newly designed logo to create a polished, professional 2-sided business card for this IT Services company.

Target Market(s)

IT Professionals many in the telecommunications and medical industries.

Industry/Entity Type

Business

Requirements
Must have
• Use of new logo, identified color palette and font: Albertus MT Std Regular.

```html
<!DOCTYPE html>
<html lang="en">
<head>
<meta charset="utf-8">
<title>Velmont Systems Business Card</title>
<link href="https://fonts.googleapis.com/css2?family=Open+Sans:wght@400;600;700&display=swap" rel="stylesheet">
<style>
  :root {
    --backdrop: #c9cacc;
    --ink: #1a1a1a;
    --navy: #1e3f9e;
    --royal: #2c55b8;
    --sky: #6e9fd8;
    --cyan: #00aeef;
    --rule: #b9bcc2;
    --paper: #ffffff;
  }
  * { margin: 0; padding: 0; box-sizing: border-box; }
  html, body { width: 1200px; height: 900px; overflow: hidden; }
  body {
    background: var(--backdrop);
    font-family: "Open Sans", Arial, sans-serif;
    position: relative;
  }
  .card {
    position: absolute;
    top: 180px;
    width: 330px;
    height: 540px;
    border-radius: 18px;
    overflow: hidden;
    box-shadow: 0 6px 18px rgba(0,0,0,0.18);
  }
  .card-front { left: 230px; }
  .card-back { left: 640px; background: var(--paper); }
  .card-art { position: absolute; inset: 0; width: 100%; height: 100%; }

  .front-artwork {
    position: absolute;
    inset: 0;
    background: linear-gradient(160deg, var(--navy) 0%, var(--royal) 35%, var(--cyan) 65%, var(--sky) 100%);
  }
  .front-brand {
    position: absolute;
    left: 0; right: 0; top: 250px;
    text-align: center;
    color: var(--paper);
    font-weight: 600;
    font-size: 22px;
    letter-spacing: 1.5px;
    line-height: 1.15;
    text-transform: uppercase;
  }

  .back-brand {
    position: absolute;
    left: 40px; top: 38px;
    display: flex; align-items: center; gap: 12px;
    color: var(--royal);
  }
  .brand-dot {
    display: block;
    width: 44px; height: 44px;
    border-radius: 50%;
    background: var(--royal);
  }
  .brand-name {
    font-weight: 600;
    font-size: 17px;
    letter-spacing: 1.5px;
    text-transform: uppercase;
  }

  .contact {
    position: absolute;
    left: 40px; top: 120px; right: 30px;
    color: var(--ink);
    font-size: 13px;
    line-height: 1.45;
  }
  .person-name {
    font-size: 20px; font-weight: 700;
    color: var(--navy);
    letter-spacing: 0.5px;
  }
  .person-role { font-size: 12px; margin-bottom: 12px; }
  .divider { border: 0; border-top: 1px solid var(--rule); width: 200px; margin: 10px 0; }
  .field-label {
    display: block;
    font-size: 10px;
    color: var(--royal);
    text-transform: uppercase;
    letter-spacing: 0.5px;
    margin-top: 6px;
  }
</style>
</head>
<body>

<section class="card card-front" aria-label="Card front">
  <div class="front-artwork" role="img" aria-label="Abstract artwork in navy, cyan and sky blue"></div>
  <div class="front-brand">Velmont<br>Systems</div>
</section>

<section class="card card-back" aria-label="Card back">
  <svg class="card-art" viewBox="0 0 330 540" aria-hidden="true">
    <path d="M0 400 C110 440 230 470 330 540 H0 Z" fill="var(--sky)"/>
    <path d="M0 425 C110 460 220 490 300 540 H0 Z" fill="var(--royal)" opacity="0.75"/>
    <path d="M0 455 C80 480 150 505 200 540 H0 Z" fill="var(--cyan)" opacity="0.55"/>
  </svg>
  <div class="back-brand">
    <span class="brand-dot"></span>
    <div class="brand-name">Velmont Systems</div>
  </div>
  <div class="contact">
    <div class="person-name">DANIEL HARWICK</div>
    <div class="person-role">Manager</div>
    <hr class="divider">
    <div>PO Box 2841</div>
    <div>Eastbrook BC, QLD, 4170</div>
    <hr class="divider">
    <span class="field-label">Phone</span>
    <div>+ 61 400 555 019</div>
    <span class="field-label">Email</span>
    <div>dharwick@velmontsystems.com</div>
    <span class="field-label">Website</span>
    <div>www.velmontsystems.com</div>
  </div>
</section>

</body>
</html>
```